Maplerise Trading Inc. needs an innovative idea for letterhead and visiting cards.

Maplerise Trading Inc. is a Canadian brand since 2007. It is a renown dealer of kids and office furniture locally. Moreover, exporting electric fixtures e.g. switches, LED's, down-lights etc. to Middle East and Africa. We have initiated a number of steps including re-branding, to boost our export in 2020. We have successfully designed our new logo a few months ago through 'Artfolio' and now we are looking for an innovative idea for a letterhead.
Some key points:
• Red, black and white are the three colors used in all our packaging and furniture. (grey is optional)
• Shouldn’t be too wide.
• Use of watermark is preferable.
• You can visit our North American site at www.mapleriseinc.com. Export website of the company will be launched soon. www.mapleriseinc.ca
• Same letterhead will be used locally and internationally.
• Our new logo and sample packaging is attached.

```html
<!DOCTYPE html>
<html lang="en">
<head>
<meta charset="utf-8">
<title>Maplerise Trading Inc. – Letterhead</title>
<link rel="stylesheet" href="https://fonts.googleapis.com/css2?family=Saira:wght@400&display=swap">
<style>
  :root {
    --paper: #ffffff;
    --red-deep: #7e151b;
    --red: #9c1c25;
    --charcoal: #4a4b4d;
    --mist: #e4e5e7;
  }
  html, body {
    margin: 0;
    padding: 0;
    width: 928px;
    height: 1200px;
    overflow: hidden;
    background: var(--paper);
  }
  .letterhead {
    position: relative;
    width: 928px;
    height: 1200px;
    background: var(--paper);
    overflow: hidden;
  }
  .letterhead__frame {
    position: absolute;
    inset: 0;
    width: 928px;
    height: 1200px;
  }
  .edge { fill: var(--mist); }
  .edge__accent { fill: var(--charcoal); }
  .ribbon { fill: none; stroke-width: 44; stroke-linecap: butt; }
  .ribbon--deep { stroke: var(--red-deep); }
  .ribbon--bright { stroke: var(--red); }

  .brand {
    position: absolute;
    top: 22px;
    right: 90px;
    display: flex;
    align-items: center;
    gap: 22px;
  }
  .brand__mark {
    width: 100px;
    height: 100px;
    background: var(--red);
    border-radius: 6px;
  }
  .brand__name {
    margin: 0;
    font-family: "Saira", sans-serif;
    font-weight: 400;
    font-size: 50px;
    line-height: 52px;
    letter-spacing: 3px;
    color: var(--charcoal);
    text-transform: uppercase;
  }
  .brand__name span { display: block; }
</style>
</head>
<body>
  <main class="letterhead">
    <svg class="letterhead__frame" viewBox="0 0 928 1200" aria-hidden="true">
      <rect class="edge" x="0" y="260" width="40" height="940"/>
      <polygon class="edge__accent" points="0,300 40,280 40,690 0,710"/>

      <rect class="edge" x="888" y="0" width="40" height="1200"/>
      <polygon class="edge__accent" points="888,510 928,490 928,880 888,900"/>

      <polyline class="ribbon ribbon--deep" points="20,-20 128,150"/>
      <polyline class="ribbon ribbon--bright" points="128,150 10,310"/>

      <polyline class="ribbon ribbon--bright" points="940,890 810,1045"/>
      <polyline class="ribbon ribbon--deep" points="810,1045 940,1215"/>
    </svg>

    <header class="brand">
      <div class="brand__mark"></div>
      <h1 class="brand__name"><span>Maplerise</span><span>Trading</span></h1>
    </header>
  </main>
</body>
</html>
```